We are looking for a simple design that would be uplifting for
upscale drug addicts

MERIDIAN CIRCLE

PLEASE SEE THE LINK FOR TAG LINE AND CONTENT

thank you.

here is all the actual info we need and we want something like this...

http://assets.qlm.brivostore.com/rest/items/7c2910e5b337de81f94a02bd57e644163ab9fe0a6712?uid=bd31c9e2f7a04c18b6e0d44721fa93c5%2fdrafts&expires=1408211537&signature=kTp4WmQxNvLzHa8YbEoRcJsGf2B%3d

The shape and colors don't have to be like what I posted it is only an example.

Target Market(s)

Wall Street, internet and creative types, men, early 30's,
upwardly mobile, drug addicts

current site

bkltornavel.com

now launching new name Meridian Circle

Industry/Entity Type

Drug

Requirements
Must have
• upscale look, great font
Should not have
• a corporate look but should not look like a clinic.

```html
<!DOCTYPE html>
<html lang="en">
<head>
<meta charset="utf-8">
<title>Meridian Circle – Business Cards</title>
<link rel="stylesheet" href="https://fonts.googleapis.com/css2?family=Archivo+Black&family=Arimo:wght@400;700&display=swap">
<style>
  :root {
    --backdrop: #3b2618;
    --lime: #8cc63f;
    --green: #0b9444;
    --yellow: #f8c40c;
    --purple: #5e3a7f;
    --red: #d8281d;
    --ink: #2b1a10;
    --white: #ffffff;
  }
  * { margin: 0; padding: 0; box-sizing: border-box; }
  html, body { width: 1200px; height: 811px; overflow: hidden; }
  body { background: var(--backdrop); font-family: "Arimo", Arial, sans-serif; }

  .sheet {
    position: absolute; left: 316px; top: 143px;
    display: grid; grid-template-columns: 277px 277px;
    grid-auto-rows: 168px; column-gap: 13px; row-gap: 10px;
  }
  .card { position: relative; width: 277px; height: 168px; overflow: hidden; }
  .card svg.card-art { position: absolute; inset: 0; width: 100%; height: 100%; }
  .card .text { position: absolute; color: var(--white); white-space: nowrap; }

  .card .brand {
    left: 0; right: 0; top: 11px; text-align: center;
    font-family: "Archivo Black", "Arial Black", sans-serif;
    font-size: 14px; letter-spacing: 0.3px;
  }
  .card .tagline {
    left: 0; right: 0; top: 27px; text-align: center;
    font-size: 7px; font-weight: 700; line-height: 8.5px;
  }
  .card .person { left: 20px; top: 90px; font-size: 10px; }
  .card .person::after {
    content: ""; display: block; width: 104px; height: 1px;
    background: var(--white); margin-top: 1px;
  }
  .card .role { left: 20px; top: 104px; font-size: 6px; font-weight: 700; }
  .card .address { left: 20px; top: 116px; font-size: 6px; font-weight: 700; line-height: 8px; }
  .card .phones { right: 24px; top: 116px; font-size: 6px; font-weight: 700; line-height: 8px; }
  .card .email-front { left: 20px; top: 148px; font-size: 6px; font-weight: 700; }
  .card .email-back { left: 0; right: 0; top: 54px; text-align: center; font-size: 9px; }

  .front-green .text.brand { color: var(--white); }
  .front-green .text.tagline { color: var(--ink); }
  .front-purple .text.brand,
  .front-purple .text.tagline { color: var(--purple); }
  .front-red .text.brand,
  .front-red .text.tagline { color: var(--red); }
</style>
</head>
<body>
<svg width="0" height="0" style="position:absolute">
  <defs>
    <radialGradient id="glow">
      <stop offset="0" stop-color="#fff" stop-opacity="0.95"/>
      <stop offset="0.35" stop-color="#fff" stop-opacity="0.45"/>
      <stop offset="1" stop-color="#fff" stop-opacity="0"/>
    </radialGradient>
    <g id="spark">
      <circle r="26" fill="url(#glow)"/>
      <path d="M-13 0H13M0-13V13M-8-8L8 8M-8 8L8-8" stroke="#fff" stroke-width="1" stroke-linecap="round"/>
      <path d="M-18 0H18M0-10V10" stroke="#fff" stroke-width="0.6"/>
    </g>
  </defs>
</svg>

<main class="sheet">
  <section class="card front front-green">
    <svg class="card-art" viewBox="0 0 277 168" aria-hidden="true">
      <rect width="277" height="168" fill="var(--lime)"/>
      <path d="M0 78 Q150 28 277 72 V168 H0Z" fill="var(--green)"/>
      <path d="M0 78 Q150 28 277 72" fill="none" stroke="#fff" stroke-width="1.4"/>
      <use href="#spark" x="200" y="54"/>
    </svg>
    <p class="text brand">MERIDIAN CIRCLE</p>
    <p class="text tagline">We walk beside you every step of the way<br>toward lasting recovery</p>
    <p class="text person">Daniel Moreau, CASAC</p>
    <p class="text role">Program Coordinator</p>
    <p class="text address">418 Alder St, Suite 304<br>Hudson, NY 12534</p>
    <p class="text phones">555 014 2290<br>555 014 2291</p>
    <p class="text email-front">counselor@harborlinewell.com</p>
  </section>
  <section class="card back back-green">
    <svg class="card-art" viewBox="0 0 277 168" aria-hidden="true">
      <rect width="277" height="168" fill="var(--green)"/>
      <path d="M0 80 Q140 150 277 96 V168 H0Z" fill="var(--lime)"/>
      <path d="M0 80 Q140 150 277 96" fill="none" stroke="#fff" stroke-width="1.4"/>
      <use href="#spark" x="200" y="112"/>
    </svg>
    <p class="text email-back">counselor@harborlinewell.com</p>
  </section>

  <section class="card front front-purple">
    <svg class="card-art" viewBox="0 0 277 168" aria-hidden="true">
      <rect width="277" height="168" fill="var(--yellow)"/>
      <path d="M0 78 Q150 28 277 72 V168 H0Z" fill="var(--purple)"/>
      <path d="M0 78 Q150 28 277 72" fill="none" stroke="#fff" stroke-width="1.4"/>
      <use href="#spark" x="200" y="54"/>
    </svg>
    <p class="text brand">MERIDIAN CIRCLE</p>
    <p class="text tagline">We walk beside you every step of the way<br>toward lasting recovery</p>
    <p class="text person">Daniel Moreau, CASAC</p>
    <p class="text role">Program Coordinator</p>
    <p class="text address">418 Alder St, Suite 304<br>Hudson, NY 12534</p>
    <p class="text phones">555 014 2290<br>555 014 2291</p>
    <p class="text email-front">counselor@harborlinewell.com</p>
  </section>
  <section class="card back back-purple">
    <svg class="card-art" viewBox="0 0 277 168" aria-hidden="true">
      <rect width="277" height="168" fill="var(--purple)"/>
      <path d="M0 80 Q140 150 277 96 V168 H0Z" fill="var(--yellow)"/>
      <path d="M0 80 Q140 150 277 96" fill="none" stroke="#fff" stroke-width="1.4"/>
      <use href="#spark" x="200" y="112"/>
    </svg>
    <p class="text email-back">counselor@harborlinewell.com</p>
  </section>

  <section class="card front front-red">
    <svg class="card-art" viewBox="0 0 277 168" aria-hidden="true">
      <rect width="277" height="168" fill="var(--yellow)"/>
      <path d="M0 78 Q150 28 277 72 V168 H0Z" fill="var(--red)"/>
      <path d="M0 78 Q150 28 277 72" fill="none" stroke="#fff" stroke-width="1.4"/>
      <use href="#spark" x="200" y="54"/>
    </svg>
    <p class="text brand">MERIDIAN CIRCLE</p>
    <p class="text tagline">We walk beside you every step of the way<br>toward lasting recovery</p>
    <p class="text person">Daniel Moreau, CASAC</p>
    <p class="text role">Program Coordinator</p>
    <p class="text address">418 Alder St, Suite 304<br>Hudson, NY 12534</p>
    <p class="text phones">555 014 2290<br>555 014 2291</p>
    <p class="text email-front">counselor@harborlinewell.com</p>
  </section>
  <section class="card back back-red">
    <svg class="card-art" viewBox="0 0 277 168" aria-hidden="true">
      <rect width="277" height="168" fill="var(--red)"/>
      <path d="M0 80 Q140 150 277 96 V168 H0Z" fill="var(--yellow)"/>
      <path d="M0 80 Q140 150 277 96" fill="none" stroke="#fff" stroke-width="1.4"/>
      <use href="#spark" x="200" y="112"/>
    </svg>
    <p class="text email-back">counselor@harborlinewell.com</p>
  </section>
</main>
</body>
</html>
```